南谷 睦月というペンネームで活動しているものです。

本業は組織・人財開発領域に特化した支援を行う会社において、
企画の提案、プロジェクトマネジメント、依頼後の進捗管理など、
お客様の中に自身も入りながら、経営を変えていくような支援を行っています。

ご依頼をさせていただく表紙デザインですが、
9月16日にPagoraにて、下記の内容を発行いたしました。
============================
現場を変える人が大切にする4つの視点:
~挑戦した人々の物語から静かに学び取る~

www.bookvale-store.jp/item/Q72KD4MX3N
こちらの内容について、発行に向けた表紙手配が間に合わなかったこともあり、
一旦はデザインを自身で考え、発行をいたしましたが、
表紙は書籍の顔ということもあり、作成依頼を進めることに決めました。

デザイン制作にあたって検討いただきたいのは下記2点です。

検討に当たってのポイントは下記2点です。
① 悩みに対しての答えが見つかるような印象を持てる
② あまり複雑すぎないデザインであること

① 悩みに対しての答えが見つかるような印象を持てる
・取り上げたPagoraでは、スキル・ノウハウ本ではなく、
実践されている方が直面されたエピソードをもとにして、
悩みを解決するためのヒントを取り上げています。
そのようなニュアンスが感じられるようなデザインに期待です。

② あまり複雑なデザインではないこと
・凝ったデザインよりは、わかりやすいデザインを好む方です。
複雑なカラーよりは、色を限りながらも、与えられた題材に対しての
表現を頂けるようなデザインが好みではあります。
※ が、良いものが出てくれば、それ限りではございませんので、
あくまで、現時点の好みとしてお伝えを致します

最終的に今回のコンペでは「R_hoshidaさん」のデザインを採用させて頂きます。
重視した点は改めて、下記の2点がベースとなります。
① 悩みに対しての答えが見つかるような印象を持てる
② あまり複雑なデザインではないこと
絵で①のイメージを喚起しつつ、今回の書籍で押し出していることを文字で強調いただく構成となっており、②の点からも適切と考えて採択をさせて頂きました。

改めて、この度はご提案をいただきましてありがとうございます。

引き続き、個人的な目標としては3か月~6か月に1回の頻度で、
Pagora向けの発行物を執筆していく予定です。
また、このような形でご支援の相談をさせていただきますので、
よろしければ是非、お力添えをどうぞお願い申し上げます。

```html
<!DOCTYPE html>
<html lang="ja">
<head>
<meta charset="UTF-8">
<title>現場を変える人が大切にする4つの視点</title>
<link rel="stylesheet" href="https://fonts.googleapis.com/css2?family=Noto+Sans+JP:wght@400;500;700;900&display=swap">
<style>
  :root {
    --paper: #ffffff;
    --ink: #1a1a1a;
    --accent: #d8141c;
    --muted: #666666;
    --art-light: #ececec;
    --art-mid: #c9c9c9;
  }
  html, body {
    margin: 0;
    padding: 0;
    overflow: hidden;
    background: var(--paper);
  }
  .cover {
    position: relative;
    width: 750px;
    height: 1200px;
    overflow: hidden;
    background: var(--paper);
    font-family: "Noto Sans JP", sans-serif;
    color: var(--ink);
  }
  .speech-bubble {
    position: absolute;
    left: 110px;
    top: 8px;
    width: 420px;
    height: 130px;
  }
  .subtitle {
    position: absolute;
    left: 130px;
    top: 28px;
    width: 380px;
    margin: 0;
    text-align: center;
    font-size: 26px;
    font-weight: 700;
    line-height: 1.35;
    color: var(--muted);
  }
  .art {
    position: absolute;
  }
  .art-presenter {
    left: 95px;
    top: 140px;
    width: 290px;
    height: 200px;
    background: radial-gradient(ellipse at 50% 45%, var(--art-mid), var(--art-light) 70%, transparent 72%);
  }
  .art-worried {
    left: 260px;
    top: 995px;
    width: 220px;
    height: 110px;
    background: radial-gradient(ellipse at 50% 60%, #9a9a9a, var(--art-light) 70%, transparent 72%);
  }
  .title {
    position: absolute;
    margin: 0;
    writing-mode: vertical-rl;
    font-weight: 900;
    line-height: 1;
    letter-spacing: 0.02em;
  }
  .title-main {
    right: 26px;
    top: 120px;
    font-size: 92px;
    color: var(--accent);
  }
  .title-sub {
    right: 150px;
    top: 170px;
    font-size: 76px;
    color: var(--ink);
  }
  .title-number {
    color: var(--accent);
    font-size: 90px;
  }
  .worries {
    position: absolute;
    right: 275px;
    top: 330px;
    margin: 0;
    padding: 0;
    list-style: none;
    display: flex;
    flex-direction: row-reverse;
    align-items: flex-start;
    gap: 4px;
  }
  .worry {
    writing-mode: vertical-rl;
    font-size: 24px;
    font-weight: 700;
    line-height: 1.15;
    letter-spacing: 0;
  }
  .worry:nth-child(2) { margin-top: 25px; }
  .worry:nth-child(3) { margin-top: 50px; }
  .worry:nth-child(4) { margin-top: 75px; }
  .worry:nth-child(5) { margin-top: 95px; }
  .worry:nth-child(6) { margin-top: 115px; }
  .worry:nth-child(7) { margin-top: 130px; }
  .author {
    position: absolute;
    left: 45px;
    bottom: 28px;
    margin: 0;
    display: flex;
    align-items: baseline;
    gap: 26px;
  }
  .author-name {
    font-size: 54px;
    font-weight: 900;
    letter-spacing: 0.05em;
  }
  .author-roman {
    font-size: 30px;
    font-weight: 500;
  }
</style>
</head>
<body>
<main class="cover">
  <svg class="speech-bubble" viewBox="0 0 420 130" aria-hidden="true">
    <path d="M30 8 H390 Q412 8 412 30 V88 Q412 108 390 108 H250 L232 128 L222 108 H30 Q8 108 8 88 V30 Q8 8 30 8 Z"
          fill="#ffffff" stroke="#555555" stroke-width="3"/>
  </svg>
  <p class="subtitle">~挑戦した人々の物語から<br>静かに学び取る~</p>

  <div class="art art-presenter" role="img" aria-label="腕を曲げて自信を示すスーツ姿の男性と電球のイラスト"></div>

  <h1 class="title title-main">現場を変える人が</h1>
  <p class="title title-sub">大切にする<span class="title-number">4</span>つの視点</p>

  <ul class="worries">
    <li class="worry">組織を超えた協力が得られない…</li>
    <li class="worry">上からまた指示が来た</li>
    <li class="worry">何を調べればいいんだ…</li>
    <li class="worry">経営層の許可が下りない</li>
    <li class="worry">どうやって進めれば…</li>
    <li class="worry">会議で時間だけが過ぎていく…</li>
    <li class="worry">何を説明すれば相手にわかってもらえるのか…</li>
  </ul>

  <div class="art art-worried" role="img" aria-label="机で頭を抱えて悩む男性のイラスト"></div>

  <p class="author">
    <span class="author-name">南谷 睦月</span>
    <span class="author-roman">Minamitani Mutsuki</span>
  </p>
</main>
</body>
</html>
```